Bright Ember Publicity is a new boutique Press Office with a small roster of well-chosen clients across an array of disciplines; from Art and Technology to Restaurants and Fashion. Based in Greenpoint Brooklyn, Bright Ember Publicity achieves outstanding results through hard work, tenacity, efficiency and a sense of humor. We need a simple, versatile and classic design. We would like each side of the card to be white text on a black background.

Boutique

```html
<!DOCTYPE html>
<html lang="en">
<head>
<meta charset="utf-8">
<title>Bright Ember Publicity — Business Card</title>
<link href="https://fonts.googleapis.com/css2?family=Open+Sans:wght@400;600&display=swap" rel="stylesheet">
<style>
  :root {
    --canvas: #2e2e2f;
    --card-top: #2a2b2c;
    --card-base: #141515;
    --ink: #ffffff;
    --ink-soft: #e9e9e9;
    --ink-faint: #6f7173;
    --icon-fill: #ffffff;
    --icon-glyph: #161717;
  }
  * { box-sizing: border-box; margin: 0; padding: 0; }
  html, body {
    width: 1200px; height: 1200px; overflow: hidden;
    background: var(--canvas);
    font-family: "Open Sans", Arial, sans-serif;
  }
  .stage {
    position: relative; width: 1200px; height: 1200px;
    display: flex; align-items: center; justify-content: center; gap: 60px;
  }
  .card {
    position: relative; width: 420px; height: 735px;
    background: radial-gradient(ellipse at 50% 25%, var(--card-top) 0%, var(--card-base) 75%);
    box-shadow: 0 18px 40px rgba(0,0,0,0.45);
    color: var(--ink);
    text-align: center;
  }
  .brand {
    position: absolute; left: 0; right: 0; top: 92px;
    display: flex; flex-direction: column; align-items: center; gap: 14px;
  }
  .brand__mark {
    width: 14px; height: 14px; border-radius: 50%;
    background: var(--ink);
  }
  .brand__name {
    font-weight: 400; font-size: 22px; letter-spacing: 0.22em;
    text-transform: uppercase; line-height: 1.5;
    color: var(--ink);
  }
  .card--back .brand { top: 300px; }
  .card--back .brand__mark { background: var(--ink-faint); }
  .card--back .brand__name { color: var(--ink-faint); }

  .person { position: absolute; left: 0; right: 0; top: 420px; }
  .person__name { font-weight: 600; font-size: 24px; line-height: 1.2; }
  .person__role { font-weight: 400; font-size: 19px; color: var(--ink-soft); line-height: 1.3; }

  .contact { position: absolute; left: 0; right: 0; top: 540px; }
  .contact__icons { display: flex; justify-content: center; gap: 8px; margin-bottom: 8px; }
  .contact__icons svg { width: 24px; height: 24px; }
  .contact__line { font-size: 17px; line-height: 1.3; color: var(--ink-soft); }

  .address {
    position: absolute; left: 0; right: 0; bottom: 28px;
    font-size: 16px; color: var(--ink-soft);
  }
</style>
</head>
<body>
<main class="stage">
  <section class="card card--front" aria-label="Card front">
    <div class="brand">
      <span class="brand__mark"></span>
      <span class="brand__name">Bright Ember<br>Publicity</span>
    </div>

    <div class="person">
      <p class="person__name">Daniel Hart</p>
      <p class="person__role">President</p>
    </div>

    <div class="contact">
      <div class="contact__icons">
        <svg viewBox="0 0 24 24" aria-label="Phone" role="img">
          <circle cx="12" cy="12" r="12" fill="var(--icon-fill)"/>
          <path d="M8.6 6.5l1.6 2.4-1 1.1c.6 1.5 1.8 2.7 3.3 3.3l1.1-1 2.4 1.6-.6 1.8c-3.9-.2-7.2-3.5-7.4-7.4z" fill="var(--icon-glyph)"/>
        </svg>
        <svg viewBox="0 0 24 24" aria-label="Email" role="img">
          <circle cx="12" cy="12" r="12" fill="var(--icon-fill)"/>
          <rect x="6.5" y="8" width="11" height="8" fill="var(--icon-glyph)"/>
          <path d="M6.5 8.3l5.5 4.2 5.5-4.2" fill="none" stroke="var(--icon-fill)" stroke-width="1"/>
        </svg>
        <svg viewBox="0 0 24 24" aria-label="Website" role="img">
          <circle cx="12" cy="12" r="12" fill="var(--icon-fill)"/>
          <circle cx="12" cy="12" r="5.5" fill="none" stroke="var(--icon-glyph)" stroke-width="1.4"/>
          <ellipse cx="12" cy="12" rx="2.3" ry="5.5" fill="none" stroke="var(--icon-glyph)" stroke-width="1.2"/>
          <line x1="6.5" y1="12" x2="17.5" y2="12" stroke="var(--icon-glyph)" stroke-width="1.2"/>
        </svg>
      </div>
      <p class="contact__line">718 555 0142</p>
      <p class="contact__line">hello@brightember.com</p>
      <p class="contact__line">www.brightember.com</p>
    </div>

    <p class="address">210 Kent Street, Brooklyn, NY 11222</p>
  </section>

  <section class="card card--back" aria-label="Card back">
    <div class="brand">
      <span class="brand__mark"></span>
      <span class="brand__name">Bright Ember<br>Publicity</span>
    </div>
  </section>
</main>
</body>
</html>
```